Business Card Design

I'm a Naturopathic Physician specializing in the treatment of autoimmune disorders, supportive cancer care and stress, anxiety and depressive disorders.

I practice out of 3 clinic locations and I want a business card design which can be easily changed to include 3 clinic locations, addresses, and contact info.

My website is VeltarisHealth.com and this will promote me personally as a specialist in these treatment areas. I would like one side of the business card to promote this site with the tag line "Specializing in Immune and Related Disorders"

REVIEW THE DESCRIPTION AND UPLOADS FOR MY DESIGN STYLE PREFERENCES.

Industry/Entity Type

Clinic

Colors
9bcb3c
fbed22
0455a3

Requirements
Must have
• Would prefer a vertical design.
Would like bold, simple colors and contrasts

Please visit http://plovexa.com/veltarishealth/ for some color and design "feel"

Do not feel the Designs HAVE to have the logo in it... I want SIMPLE, CLEAN and BOLD design so if the Logo makes the designs too busy, please omit

Dr. Marcus Fenholt BSc ND
Naturopathic Physician

"Clinic Name"
"Clinic Address"
"Clinic Tel"
"Clinic E-Mail"
"Clinic Website"

Please review the PDF for design styles I prefer.

Please Note: Once I determine if there are design concepts worthy of going forward with, I will forward specific contact and clinic information at that time for final design

```html
<!DOCTYPE html>
<html lang="en">
<head>
<meta charset="UTF-8">
<title>Veltaris Health – Business Card</title>
<link rel="stylesheet" href="https://fonts.googleapis.com/css2?family=Questrial&family=Didact+Gothic&display=swap">
<style>
  :root {
    --brand-blue: #0455a3;
    --brand-blue-deep: #034a8f;
    --brand-green: #9bcb3c;
    --ink-grey: #6b6b6b;
    --soft-grey: #a9a9a9;
    --card-white: #ffffff;
    --stage-top: #ffffff;
    --stage-bottom: #e4e4e4;
  }
  * { margin: 0; padding: 0; box-sizing: border-box; }
  html, body {
    width: 1200px;
    height: 1000px;
    overflow: hidden;
  }
  body {
    background: radial-gradient(ellipse at 50% 40%, var(--stage-top) 0%, var(--stage-bottom) 100%);
    font-family: "Questrial", "Didact Gothic", sans-serif;
    position: relative;
  }
  .card {
    position: absolute;
    left: 280px;
    width: 640px;
    height: 340px;
    border-radius: 30px;
    overflow: hidden;
    box-shadow: 0 6px 14px rgba(0, 0, 0, 0.22);
  }

  /* Front side */
  .card-front {
    top: 110px;
    background: var(--brand-blue);
  }
  .pattern-field {
    position: absolute;
    inset: 0;
    background: linear-gradient(160deg, var(--brand-blue) 0%, var(--brand-blue-deep) 100%);
  }
  .brand-mark {
    position: absolute;
    top: 78px;
    left: 0;
    right: 0;
    display: flex;
    align-items: center;
    justify-content: center;
    gap: 14px;
  }
  .brand-dot {
    width: 34px;
    height: 34px;
    border-radius: 50%;
    background: var(--brand-green);
  }
  .brand-name {
    font-size: 30px;
    color: var(--card-white);
    letter-spacing: 0.5px;
  }
  .tagline-band {
    position: absolute;
    left: 0;
    right: 0;
    top: 228px;
    height: 38px;
    background: var(--brand-green);
    display: flex;
    align-items: center;
    justify-content: center;
  }
  .tagline {
    font-size: 19px;
    color: var(--brand-blue);
    letter-spacing: 1px;
    font-weight: 700;
  }

  /* Back side */
  .card-back {
    top: 530px;
    background: var(--card-white);
  }
  .company-name {
    position: absolute;
    left: 48px;
    top: 122px;
    font-size: 16px;
    line-height: 25px;
    letter-spacing: 1.5px;
    color: var(--brand-blue);
    font-weight: 700;
  }
  .divider {
    position: absolute;
    left: 182px;
    top: 56px;
    width: 2px;
    height: 206px;
    background: var(--brand-blue);
  }
  .details {
    position: absolute;
    left: 212px;
    top: 52px;
    right: 20px;
  }
  .doctor-name {
    font-size: 26px;
    color: var(--ink-grey);
    letter-spacing: 1.2px;
    font-weight: 400;
  }
  .doctor-title {
    font-size: 15px;
    color: var(--soft-grey);
    letter-spacing: 1px;
    margin-top: 1px;
  }
  .contact-list {
    list-style: none;
    font-size: 17px;
    color: var(--ink-grey);
    letter-spacing: 1px;
  }
  .contact-list li {
    display: flex;
    align-items: center;
    gap: 5px;
    height: 24px;
  }
  .contact-list svg { fill: var(--brand-blue); flex: none; }
  .contact-direct { margin-top: 20px; }
  .contact-clinic { margin-top: 44px; }
  .contact-clinic li { gap: 9px; font-size: 18px; }
</style>
</head>
<body>

  <section class="card card-front" aria-label="Business card front">
    <div class="pattern-field" role="img" aria-label="Subtle light-blue triangular line pattern on blue"></div>
    <div class="brand-mark">
      <span class="brand-dot"></span>
      <span class="brand-name">VeltarisHealth.com</span>
    </div>
    <div class="tagline-band">
      <p class="tagline">Specializing in Immune and Related Disorders</p>
    </div>
  </section>

  <section class="card card-back" aria-label="Business card back">
    <p class="company-name">COMPANY<br>NAME</p>
    <div class="divider"></div>
    <div class="details">
      <h1 class="doctor-name">Dr. Marcus Fenholt BSc ND</h1>
      <p class="doctor-title">Naturopathic Physician</p>

      <ul class="contact-list contact-direct">
        <li>
          <svg width="12" height="18" viewBox="0 0 12 18" aria-hidden="true">
            <path d="M2 0h8a2 2 0 0 1 2 2v14a2 2 0 0 1-2 2H2a2 2 0 0 1-2-2V2a2 2 0 0 1 2-2zm0 2v12h8V2H2zm4 13a1 1 0 1 0 0 2 1 1 0 0 0 0-2z"/>
          </svg>
          000 000 00000
        </li>
        <li>
          <svg width="15" height="11" viewBox="0 0 15 11" aria-hidden="true">
            <path d="M0 0h15v11H0z M1 1l6.5 5L14 1z" fill-rule="evenodd"/>
          </svg>
          dr.marcus@xxxx.com
        </li>
      </ul>

      <ul class="contact-list contact-clinic">
        <li>
          <svg width="20" height="18" viewBox="0 0 20 18" aria-hidden="true">
            <path d="M10 0l10 9h-3v9h-5v-6H8v6H3V9H0z"/>
          </svg>
          Address
        </li>
        <li>
          <svg width="20" height="14" viewBox="0 0 20 14" aria-hidden="true">
            <path d="M0 5c0-3 5-5 10-5s10 2 10 5l-1 2h-4l-1-3H6L5 7H1zM4 8h12l2 6H2zm6 1.5a2 2 0 1 0 0 4 2 2 0 0 0 0-4z"/>
          </svg>
          Contact
        </li>
      </ul>
    </div>
  </section>

</body>
</html>
```